Landing page for selling a web application used by archeologists

We are selling a web program that professional archeologists use. This program is developed and designed already. But we are now building another website for presenting this web program.
I have uploaded a pdf file that shows the mockup of the future web page. You will also find a folder containing the photos used in the mockup. You can use your own photos for the ones named with "(can be changed)".
There is another folder called "otherPhoto". You can use them if you want to do background or ambiance...
We expect a really clean, serious, and professional design.

You will see in the mockup that there is a first part (main header) followed by 6 subparts presenting the different aspect of the web app. It finishes with the last part presenting ourselves and inviting to test the program.

Here are some links to website designs that go in the direction of what we want.
https://marovel.quintabrook.com/startup/#home
https://www.pathcrafter-wp. com/mobileapp-landing/
https://en.dravelpoint.com/
https://assets.korinthub.com/en/plyva-saas-software-landing-html5-page-template-RT4WN7/preview

Don't hesitate to contact me if you need more explanations.
As requested by a designer, I also added 2 print screen of the app that we are selling.
Updates

Feel free to use your own photos for background images for example...

Target Market(s)

Professional archaeologists

Industry/Entity Type

Archeology

Number of Pages Required

1 page

Colors
0054AA
0677BA
7BADD7
CADEEF
E8F1F8
0094D4
00A9DD
6FCCEA
C7EBF8
E9F6FB
FFC000
F8CF3A
FAE287
FDF2CF
FEFAEE

Requirements
Must have
• A professional look that says that our company is large and serious

```html
<!DOCTYPE html>
<html lang="en">
<head>
<meta charset="utf-8">
<title>Stratavault – Technology Serving Archeology</title>
<link href="https://fonts.googleapis.com/css2?family=DM+Sans:wght@400;500;700&family=Libre+Caslon+Text&display=swap" rel="stylesheet">
<style>
  :root{
    --amber:#ffc252;
    --ink:#2b2b2b;
    --mist:#f5f5f5;
    --canvas:#ebebeb;
    --muted:#8a8a8a;
    --line:#e4e4e4;
    --sky-top:#5b86c4;
    --sky-bottom:#9db8dc;
  }
  *{box-sizing:border-box;margin:0;padding:0}
  html,body{width:1200px;height:3746px;overflow:hidden}
  body{background:var(--canvas);font-family:"DM Sans",sans-serif;color:var(--ink)}
  .page{position:absolute;left:250px;top:65px;width:700px;height:3615px;background:#fff;box-shadow:0 2px 18px rgba(0,0,0,.06);overflow:hidden}
  .section{position:relative;width:700px}
  .abs{position:absolute}
  .placeholder{position:absolute}

  .brand{font-weight:500;font-size:14px;color:var(--ink)}
  .title{font-size:19px;font-weight:400;color:var(--ink);white-space:nowrap}
  .title b{font-weight:700}
  .sub{font-size:9.5px;color:var(--muted)}
  .text{font-size:7.5px;line-height:1.6;color:#555;width:240px}
  .btn{display:inline-flex;align-items:center;justify-content:center;height:22px;padding:0 14px;border-radius:11px;font-size:6.5px;font-weight:500;letter-spacing:.3px;text-transform:uppercase;white-space:nowrap}
  .btn-fill{background:var(--amber);color:#fff}
  .btn-line{border:1px solid var(--amber);color:var(--ink);background:#fff}
  .btn-center{left:50%;transform:translateX(-50%)}
  .caption{font-family:"Libre Caslon Text",serif;font-size:7.5px;line-height:1.55;color:#333;display:flex;align-items:center;gap:10px}
  .caption::after{content:"";width:9px;height:9px;border-radius:50%;background:var(--ink);flex:none}

  .hero{height:431px;background:linear-gradient(180deg,#f7f6f4 0%,#efece8 45%,#e9e5df 100%);border-bottom:2px solid var(--amber)}
  .hero-bg{left:0;top:50px;width:700px;height:381px;background:linear-gradient(180deg,rgba(240,236,230,.0),rgba(214,206,196,.55))}
  .nav{left:95px;top:14px;width:520px;height:20px;display:flex;align-items:center;justify-content:space-between}
  .nav-links{display:flex;align-items:center;gap:18px;font-size:6.5px;color:#555;white-space:nowrap}
  .login{height:18px;width:52px;border-radius:9px;background:var(--amber);color:#fff;font-size:6px;display:flex;align-items:center;justify-content:center;font-weight:500}
  .hero-title{left:0;top:128px;width:700px;text-align:center;font-size:30px;font-weight:500}
  .hero-title .hl{color:var(--amber)}
  .hero-sub{left:0;top:180px;width:700px;text-align:center;font-size:8px;color:#777}
  .hero-cta{top:213px}
  .hero-devices{left:160px;top:292px;width:374px;height:205px;background:linear-gradient(135deg,#3a3a3a,#8c8c8c 55%,#d9d9d9);border-radius:6px;opacity:.9}

  .rule{left:95px;width:515px;height:1px;background:var(--line)}

  .entry{height:418px}
  .grey{background:var(--mist)}
  .dark{background:var(--ink)}
  .analysis{height:325px}
  .publication{height:461px}
  .view{height:403px}
  .forum{height:470px}
  .archive{height:403px}
  .about{height:557px;background:linear-gradient(180deg,var(--sky-top),var(--sky-bottom))}
  .footer{height:146px}

  .center{left:0;width:700px;text-align:center}
  .pub-title,.pub-title b{color:var(--amber)}

  .card{position:absolute;top:175px;width:160px;height:223px;background:#fff;padding:26px 16px}
  .card h3{font-size:8px;font-weight:700;line-height:1.4;margin:14px 0 12px}
  .card p{font-size:6px;line-height:1.85;color:#777}
  .about-head{font-size:20px;font-weight:500;color:#fff;line-height:1.3}
  .about-text{font-size:6.5px;line-height:1.8;color:#eef3fa}
  .trial{left:95px;top:470px;font-size:18px;font-weight:500;color:#fff;line-height:1.35}
  .trial .hl{color:var(--amber)}

  .foot-links{left:95px;top:86px;display:flex;gap:18px;font-size:6.5px;color:#666}
  .foot-brand{left:0;width:700px;top:80px;text-align:center;font-size:13px;font-weight:500}
  .copy{right:95px;top:86px;font-size:6px;color:#666}
</style>
</head>
<body>
<main class="page">

  <header class="section hero">
    <div class="placeholder hero-bg" role="img" aria-label="Faded photo of an ancient Roman amphitheatre"></div>
    <nav class="abs nav">
      <span class="brand">Stratavault</span>
      <div class="nav-links">
        <span>Solution</span><span>Price</span><span>Contact &nbsp;| &nbsp;EN ⌄</span>
        <span class="login">LOGIN</span>
      </div>
    </nav>
    <h1 class="abs hero-title">Technology <span class="hl">Serving</span> Archeology</h1>
    <p class="abs hero-sub">Stratavault the solution to input, analyse and promote the archaeological heritage</p>
    <a class="abs btn btn-line btn-center hero-cta">Learn more</a>
    <div class="placeholder hero-devices" role="img" aria-label="Two desktop screens showing the application's map and data views"></div>
  </header>

  <section class="section entry">
    <div class="abs rule" style="top:117px"></div>
    <h2 class="abs title" style="left:95px;top:210px">Strata <b>Entry</b></h2>
    <p class="abs sub" style="left:95px;top:252px">Capture of archeological information</p>
    <p class="abs text" style="left:95px;top:270px">How to make more, faster, with the same amount of resources?</p>
    <a class="abs btn btn-fill" style="left:95px;top:309px">More details</a>
    <div class="placeholder" role="img" aria-label="Two tablets displaying excavation photos and data entry forms" style="left:323px;top:189px;width:334px;height:120px;background:linear-gradient(135deg,#d8d8d8,#f2f2f2 50%,#bfb6aa);border-radius:6px"></div>
    <p class="abs caption" style="left:416px;top:336px">Stratavault as force multiplier</p>
  </section>

  <section class="section analysis grey">
    <div class="placeholder" role="img" aria-label="Browser windows showing charts of archaeological finds per period" style="left:82px;top:50px;width:254px;height:182px;background:linear-gradient(160deg,#ffffff,#e6ebf2 60%,#c9d4e6);border:1px solid #ddd"></div>
    <p class="abs caption" style="left:136px;top:245px;width:160px">Stratavault as an intuitive solution to complex analysis problems</p>
    <h2 class="abs title" style="left:386px;top:93px">Strata <b>Analysis</b></h2>
    <p class="abs sub" style="left:386px;top:131px">Analysis of archeological information</p>
    <p class="abs text" style="left:386px;top:150px">How to detect hidden relationships, make sense of the information and preserve the big picture?</p>
    <a class="abs btn btn-line" style="left:386px;top:200px">More details</a>
  </section>

  <section class="section publication dark">
    <h2 class="abs title center pub-title" style="top:48px">Strata <b>Publication</b></h2>
    <p class="abs center" style="top:84px;font-size:8.5px;color:#fff">Publication of archeological information</p>
    <p class="abs center" style="top:112px;font-size:7px;color:#ddd">How to publish in a scientific format and find the information scattered among multiple publications in Pdf format?</p>
    <a class="abs btn btn-fill btn-center" style="top:144px">More details</a>
    <p class="abs caption" style="left:277px;top:188px;width:160px;color:#fff">Stratavault as a tool for publishing and searching information</p>
    <div class="placeholder" role="img" aria-label="Tablet showing a published excavation report with photos" style="left:215px;top:249px;width:269px;height:212px;background:linear-gradient(180deg,#151515 0 6px,#9a6f55 6px,#b88a6c 60px,#fafafa 60px);border:6px solid #111;border-bottom:none;border-radius:12px 12px 0 0"></div>
  </section>

  <section class="section view">
    <h2 class="abs title" style="left:95px;top:141px">Strata <b>View</b></h2>
    <p class="abs sub" style="left:95px;top:176px">Promotion of the archeological heritage</p>
    <p class="abs text" style="left:95px;top:194px">How to render the archaeological heritage accessible to the general public, as well as to the educational and tourist sectors?</p>
    <a class="abs btn btn-line" style="left:95px;top:233px">More details</a>
    <div class="placeholder" role="img" aria-label="Photo of an illuminated Roman amphitheatre at dusk" style="left:401px;top:54px;width:178px;height:254px;background:linear-gradient(180deg,#c9bfb3,#a98468 45%,#5c4a3e)"></div>
    <div class="placeholder" role="img" aria-label="Photo of an ancient carved stone relief" style="left:598px;top:70px;width:102px;height:208px;background:linear-gradient(160deg,#e2a37a,#c98b62 60%,#a96d4b)"></div>
    <p class="abs caption" style="left:433px;top:330px;width:130px">Stratavault as a mobilizing and unifying power</p>
  </section>

  <section class="section forum grey">
    <div class="placeholder" role="img" aria-label="Faint map of Europe with a network of connected specialists" style="left:60px;top:0;width:580px;height:470px;background:radial-gradient(ellipse at center,#e6e6e6 0%,#efefef 55%,rgba(245,245,245,0) 75%)"></div>
    <h2 class="abs title center" style="top:48px">Strata <b>Forum</b></h2>
    <p class="abs sub center" style="top:88px">Staying in touch with the community</p>
    <p class="abs center" style="top:112px;font-size:7px;color:#555">How to connect among specialists and exchange ideas across borders and languages?</p>
    <div class="placeholder" role="img" aria-label="Network of specialist profiles linked across the map" style="left:123px;top:157px;width:445px;height:167px;background:radial-gradient(circle at 50% 50%,#d8d8d8,rgba(230,230,230,0) 70%)"></div>
    <a class="abs btn btn-fill btn-center" style="top:362px">More details</a>
    <p class="abs caption" style="left:277px;top:396px;width:160px">StrataForum as a solution for multilingual specialist networking</p>
  </section>

  <section class="section archive">
    <div class="placeholder" role="img" aria-label="Photo of archive shelves filled with books" style="left:0;top:70px;width:59px;height:210px;background:linear-gradient(180deg,#b79c7c,#8a6f52 50%,#c9b89e)"></div>
    <div class="placeholder" role="img" aria-label="Photo of a stone tablet with an ancient Greek inscription" style="left:76px;top:53px;width:178px;height:257px;background:linear-gradient(160deg,#c9c3bc,#a8a098 55%,#8d847b)"></div>
    <p class="abs caption" style="left:106px;top:332px;width:130px">Stratavault as a solution for dispersed information</p>
    <h2 class="abs title" style="left:390px;top:139px">Strata <b>Archive</b></h2>
    <p class="abs sub" style="left:390px;top:174px">Retrieval of information</p>
    <p class="abs text" style="left:390px;top:192px;width:220px">How to find information quickly within archives in various formats (pdf, dbase, etc.)?</p>
    <a class="abs btn btn-line" style="left:390px;top:238px">More details</a>
  </section>

  <section class="section about">
    <div class="placeholder" role="img" aria-label="Photo of a glass office tower seen from below" style="left:180px;top:340px;width:340px;height:217px;background:linear-gradient(180deg,rgba(40,60,100,.15),rgba(30,45,80,.6))"></div>
    <h2 class="abs center about-head" style="top:55px">Stratavault:<br>innovative, reliable, at the cutting edge of technology</h2>
    <p class="abs center about-text" style="top:122px;padding:0 120px">Founded by a Swiss team of computer engineers and data analysts, Stratavault places innovation at the service of science. Its solution is to offer the latest computer tools to the world of archaeology in order to facilitate and promote the work of archaeologists.</p>

    <article class="card" style="left:95px">
      <svg width="22" height="22" viewBox="0 0 22 22"><path d="M11 2 L19 5 V11 C19 16 15 19 11 20 C7 19 3 16 3 11 V5 Z" fill="var(--amber)"/><path d="M7 11 L10 14 L15 8" stroke="#fff" stroke-width="1.8" fill="none"/></svg>
      <h3>Expertise &amp; Security<br>of a Swiss company</h3>
      <p>We bring together the most advanced technical engineering skills to deploy the right solutions for the most demanding problems. Big data input and processing, scalability, statistic analysis, deep learning and machine learning are our daily routine.</p>
    </article>
    <article class="card" style="left:269px">
      <svg width="22" height="22" viewBox="0 0 22 22"><circle cx="10" cy="7" r="5" fill="var(--amber)"/><rect x="6" y="13" width="10" height="3" rx="1.5" fill="var(--amber)"/><rect x="6" y="17" width="10" height="3" rx="1.5" fill="var(--amber)"/></svg>
      <h3>Affordable<br>prices</h3>
      <p>Budgets in archaeology are often limited. Reaching a large number of users allows advanced technological solutions that are usually very expensive to be offered at very low prices.</p>
    </article>
    <article class="card" style="left:444px">
      <svg width="22" height="22" viewBox="0 0 22 22"><rect x="2" y="3" width="18" height="12" rx="1.5" fill="var(--amber)"/><rect x="9" y="15" width="4" height="3" fill="var(--amber)"/><rect x="6" y="18" width="10" height="2" fill="var(--amber)"/><path d="M6 11 L9 8 L12 10 L16 6" stroke="#fff" stroke-width="1.4" fill="none"/></svg>
      <h3>Ongoing<br>developments</h3>
      <p>Accompanied by professional archaeologists, we are continually shaping the tool to meet their precise needs and expectations. We are always listening to new development proposals in order to solve the problems that archaeologists face on a daily basis.</p>
    </article>

    <p class="abs trial">Get now a <span class="hl">free</span> 3-month trial<br>of Stratavault</p>
    <a class="abs btn btn-fill" style="left:535px;top:475px">Contact us</a>

    <svg class="abs" style="left:0;bottom:0" width="700" height="70" viewBox="0 0 700 70" preserveAspectRatio="none"><path d="M0 30 C120 70 240 80 360 55 C480 30 600 10 700 20 V70 H0 Z" fill="#fff"/></svg>
  </section>

  <footer class="section footer">
    <div class="abs foot-links"><span>Solution</span><span>Price</span><span>Contact</span></div>
    <div class="abs foot-brand">Stratavault</div>
    <div class="abs copy">© Stratavault 2021 - All Rights Reserved</div>
  </footer>

</main>
</body>
</html>
```